Implant and Sedation Dentistry Dental Practice Signage

Design a sign that projects a relaxing competent sedation dental practice.
The practice name is TDS - Tidewater Dental Services
Practice owner is Marcus Alan Brightwell, DMD, AEGD
The logo could be used for an outdoor sign and on letterhead + business cards.
In addition, we will present seminars to other dentists under the name Tidewater Dental Seminars. We may use the same logo design with the word Services changed to Seminars.

```html
<!DOCTYPE html>
<html lang="en">
<head>
<meta charset="utf-8">
<title>Tidewater Dental Services – Sign</title>
<link rel="stylesheet" href="https://fonts.googleapis.com/css2?family=Arimo:wght@400;700&family=Questrial&family=Tinos&display=swap">
<style>
  :root {
    --navy: #153a4f;
    --navy-deep: #143a4e;
    --sky: #6ec6e4;
    --white: #ffffff;
    --ink: #163b50;
  }
  html, body {
    margin: 0;
    padding: 0;
    overflow: hidden;
    background: var(--navy);
  }
  .sign {
    position: relative;
    width: 1200px;
    height: 1000px;
    background: var(--navy-deep);
    overflow: hidden;
  }
  .hero {
    position: absolute;
    left: 0; top: 0;
    width: 1200px;
    height: 500px;
    background: var(--navy);
  }
  .hero-wave {
    position: absolute;
    left: 0; top: 0;
  }
  .brand-name {
    position: absolute;
    left: 68px;
    top: 154px;
    margin: 0;
    font-family: "Arimo", Arial, sans-serif;
    font-weight: 700;
    font-size: 31px;
    color: var(--white);
    white-space: nowrap;
  }
  .tagline {
    position: absolute;
    left: 570px;
    top: 176px;
    margin: 0;
    font-family: "Questrial", "Century Gothic", sans-serif;
    color: var(--ink);
    text-shadow: 1px 1px 0 var(--white), -1px -1px 0 var(--white), 1px -1px 0 var(--white), -1px 1px 0 var(--white);
    line-height: 1;
    white-space: nowrap;
  }
  .tagline-lead {
    font-size: 104px;
    letter-spacing: -1px;
  }
  .tagline-rest {
    font-size: 33px;
    margin-left: 8px;
  }
  .tagline-end {
    display: block;
    font-size: 58px;
    margin-left: 224px;
    margin-top: -14px;
  }
  .footer-name {
    position: absolute;
    left: 10px;
    top: 700px;
    margin: 0;
    font-family: "Tinos", "Times New Roman", serif;
    font-weight: 400;
    font-size: 47px;
    color: var(--white);
  }
  .footer-rule {
    position: absolute;
    left: 0; top: 760px;
    width: 1200px;
    height: 4px;
    background: var(--white);
  }
  .office {
    position: absolute;
    left: 10px;
    top: 774px;
    margin: 0;
    font-family: "Tinos", "Times New Roman", serif;
    font-style: normal;
    font-size: 21px;
    line-height: 29px;
    color: var(--white);
  }
  .office .contact {
    margin-top: 28px;
    font-family: "Arimo", Arial, sans-serif;
    font-size: 20px;
  }
  .doctor {
    position: absolute;
    right: 17px;
    top: 770px;
    margin: 0;
    text-align: right;
    font-family: "Tinos", "Times New Roman", serif;
    color: var(--white);
    line-height: 1;
  }
  .doctor-name { display: block; font-size: 38px; }
  .doctor-credentials { display: block; font-size: 32px; margin-top: 6px; }
</style>
</head>
<body>
  <main class="sign">
    <section class="hero">
      <svg class="hero-wave" width="1200" height="500" viewBox="0 0 1200 500" aria-hidden="true">
        <path d="M0,305 C150,345 330,275 470,195 C620,105 900,45 1200,72 L1200,498 L0,498 Z" fill="var(--sky)"/>
        <path d="M0,305 C150,345 330,275 470,195 C620,105 900,45 1200,72" fill="none" stroke="var(--white)" stroke-width="4"/>
        <line x1="0" y1="498.5" x2="1200" y2="498.5" stroke="#b9e3f1" stroke-width="1"/>
      </svg>
      <p class="brand-name">Tidewater Dental Services</p>
      <p class="tagline">
        <span class="tagline-lead">Relax</span><span class="tagline-rest">your way to a</span>
        <span class="tagline-end">better smile.</span>
      </p>
    </section>

    <h1 class="footer-name">Tidewater Dental Services</h1>
    <div class="footer-rule"></div>

    <address class="office">
      <div>Harbor Point Office</div>
      <div>218 Cypress Lane</div>
      <div>Harbor Point, FL</div>
      <div class="contact">Phone:&nbsp; 321-555-0147</div>
      <div>www.tidewaterdentalcare.com</div>
    </address>

    <p class="doctor">
      <span class="doctor-name">Dr. Marcus Brightwell</span>
      <span class="doctor-credentials">DMD, AEGD</span>
    </p>
  </main>
</body>
</html>
```